Design for Agenda app (online tool) (#102244)

Url of the app: http://notes.bluefernlab.dk

It currently has 3 main parts:
- Front: http://fernhost.dk/screencast/2015-12-01_12-53-36.png
- Dashboard: http://fernhost.dk/screencast/2015-12-01_12-54-16.png
- Meeting page: http://fernhost.dk/screencast/2015-12-01_12-54-53.png

The idea of the app is to have virtual meetings with other people, to take notes/minutes online and to share what is written.

Unregistered users can see only the front.

Registered users can see front, their own dashboard and the meetings which they created or to which they were invited.

The meeting itself has two roles - minute taker an attendee. The attendee can edit only the agenda so he should have different view for the other parts of the meeting compared to the minute taker who can edit everything.

In this doc it is described what are the elements per page which we want to have
https://files.example-docs.net/d/7qXk2LmPz9RtYv4NcBw8HsJd3FgA6eUo1KtQ5WnZ0yE/edit?usp=sharing

As you can see, there is some inconsistency between the front page and the rest of the app. We would like to make it look professional and consistent on all places.

Goal: Get new responsive design where all main parts(front page, dashboard page, meeting page and profile page) will be consistent with each other.

The design should be clean, simple and with very friendly UX.
Updates

Industry/Entity Type

Online

Number of Pages Required

3 page

Font styles to use
Sans Serif

Requirements
Must have
• - Clean and simple
• - Very friendly UX

```html
<!DOCTYPE html>
<html lang="en">
<head>
<meta charset="utf-8">
<title>Bluefern Notes – Front</title>
<link rel="stylesheet" href="https://fonts.googleapis.com/css2?family=Roboto:wght@300;400;500;700&display=swap">
<style>
  :root {
    --canvas-bg: #f8f3f6;
    --brand-pink: #f04e6e;
    --brand-rose: #e8506e;
    --brand-teal: #1fa584;
    --hero-dark: #262d36;
    --hero-mid: #3a4450;
    --white: #ffffff;
    --menu-text: #2a2a2a;
    --menu-line: #e4e4e4;
    --icon-dark: #2b323c;
  }
  * { box-sizing: border-box; margin: 0; padding: 0; }
  html, body {
    width: 1200px; height: 1000px; overflow: hidden;
    background: var(--canvas-bg);
    font-family: "Roboto", Helvetica, Arial, sans-serif;
  }
  .app-screen {
    position: absolute; left: 333px; top: 81px;
    width: 534px; height: 838px; overflow: hidden;
    background: var(--hero-dark);
  }
  .hero-photo {
    position: absolute; inset: 56px 0 0 0;
    background:
      radial-gradient(ellipse 60% 45% at 55% 30%, rgba(90,100,112,.55), transparent 70%),
      radial-gradient(ellipse 50% 30% at 55% 62%, rgba(70,80,92,.45), transparent 70%),
      linear-gradient(180deg, var(--hero-mid) 0%, var(--hero-dark) 100%);
  }
  .top-bar {
    position: absolute; left: 0; top: 0; width: 100%; height: 56px;
    background: linear-gradient(90deg, var(--brand-rose) 0%, var(--brand-teal) 100%);
  }
  .menu-toggle { position: absolute; left: 16px; top: 16px; }
  .app-name {
    position: absolute; left: 0; right: 0; top: 18px;
    text-align: center; color: var(--white);
    font-size: 17px; font-weight: 400; letter-spacing: .3px;
  }
  .nav-menu {
    position: absolute; left: 0; top: 56px; width: 184px;
    background: var(--white); list-style: none; padding: 4px 0 4px;
  }
  .nav-menu li {
    height: 39px; line-height: 39px; padding-left: 8px;
    font-size: 14px; color: var(--menu-text); letter-spacing: .6px;
    border-bottom: 1px solid var(--menu-line);
  }
  .nav-menu li:last-child { border-bottom: none; }
  .hero-text { position: absolute; left: 0; right: 0; top: 336px; text-align: center; color: var(--white); }
  .hero-title { font-size: 46px; font-weight: 400; letter-spacing: .2px; }
  .hero-subtitle { font-size: 27px; font-weight: 300; margin-top: 4px; }
  .watch-video { position: absolute; left: 0; right: 0; top: 522px; text-align: center; color: var(--white); }
  .watch-video svg { display: block; margin: 0 auto; }
  .watch-label { display: block; font-size: 29px; font-weight: 300; margin-top: 12px; }
  .auth-actions { position: absolute; top: 736px; left: 0; width: 100%; }
  .btn {
    position: absolute; width: 154px; height: 48px; border-radius: 24px;
    background: var(--brand-pink); color: var(--white);
    font-size: 14px; font-weight: 700; letter-spacing: .5px;
    text-align: center; line-height: 48px;
  }
  .btn-login { left: 94px; }
  .btn-signup { left: 278px; }
</style>
</head>
<body>
  <main class="app-screen">
    <div class="hero-photo" role="img" aria-label="Dim photo of a small potted plant on a desk"></div>

    <header class="top-bar">
      <svg class="menu-toggle" width="36" height="24" viewBox="0 0 36 24" aria-hidden="true">
        <rect x="0" y="2" width="36" height="3" fill="#fff"/>
        <rect x="0" y="11" width="36" height="3" fill="#fff"/>
        <rect x="0" y="20" width="36" height="3" fill="#fff"/>
      </svg>
      <div class="app-name">Bluefern Notes</div>
    </header>

    <ul class="nav-menu">
      <li>ABOUT</li>
      <li>FEATURES</li>
      <li>PRIVACY</li>
      <li>TERMS OF SERVICE</li>
      <li>CONTACT</li>
    </ul>

    <section class="hero-text">
      <h1 class="hero-title">Meet, Note, Share!</h1>
      <p class="hero-subtitle">Take note of all kind of events!</p>
    </section>

    <div class="watch-video">
      <svg width="74" height="74" viewBox="0 0 74 74" aria-hidden="true">
        <circle cx="37" cy="37" r="37" fill="#fff"/>
        <rect x="20" y="27" width="24" height="20" rx="3" fill="var(--icon-dark)"/>
        <polygon points="44,37 55,28 55,46" fill="var(--icon-dark)"/>
      </svg>
      <span class="watch-label">Watch Video</span>
    </div>

    <div class="auth-actions">
      <span class="btn btn-login">LOG IN</span>
      <span class="btn btn-signup">SIGN UP</span>
    </div>
  </main>
</body>
</html>
```